looking for sleek business card to standout from the crowd!

We are a young biotechnology company looking to help you personalize your health through understanding your genetic make up. We need you help in making a clean but sleek business card design using our new logo. The goal? Any time we give our cards out, people say "nice card!" The feel we are going for is "modern-techy". We don't want to come across as an old, giant pharma company, but not trying to be a hipster either.

Target Market(s)

healthcare and biotechnology industry.

Industry/Entity Type

Biotechnology

Contact Information for Business Card

Info to include on the card will be NAME, TITLE, EMAIL, PHONE. The companies website (www.morvalytics.com) should also be on the card some where. Would like the logo, when printed, to be raised.

Requirements
Must have
• The logo we have attached in the color it is in. Fonts for text should lean toward more professional/tech.
Nice to have
• Prefer white/light color background
Should not have
• cartoons, landscape backgrounds images.

```html
<!DOCTYPE html>
<html lang="en">
<head>
<meta charset="utf-8">
<title>Morvalytics Business Card</title>
<link rel="stylesheet" href="https://fonts.googleapis.com/css2?family=Exo+2:wght@700&family=Open+Sans:wght@400&display=swap">
<style>
  :root {
    --page-bg: #ededed;
    --card-bg: #ffffff;
    --navy: #1e4863;
    --bright-blue: #0b78c0;
    --mid-blue: #1668a6;
    --brand-blue: #0a6fb8;
    --text-grey: #8a8a8a;
    --deco-grey: #8d9aa5;
  }
  * { margin: 0; padding: 0; box-sizing: border-box; }
  html, body {
    width: 1200px;
    height: 1000px;
    overflow: hidden;
    background: var(--page-bg);
  }
  .business-card {
    position: absolute;
    left: 75px;
    top: 185px;
    width: 1050px;
    height: 630px;
    background: var(--card-bg);
    overflow: hidden;
  }
  .card-backdrop {
    position: absolute;
    inset: 0;
    width: 100%;
    height: 100%;
  }
  .side-wordmark {
    position: absolute;
    left: 243px;
    top: 315px;
    transform: translate(-50%, -50%) rotate(-90deg);
    font-family: "Exo 2", sans-serif;
    font-weight: 700;
    font-size: 40px;
    letter-spacing: 2px;
    color: var(--deco-grey);
    white-space: nowrap;
  }
  .brand-name {
    position: absolute;
    left: 373px;
    width: 590px;
    top: 155px;
    text-align: center;
    font-family: "Exo 2", sans-serif;
    font-weight: 700;
    font-size: 72px;
    line-height: 1;
    color: var(--brand-blue);
    white-space: nowrap;
  }
  .person {
    position: absolute;
    left: 378px;
    width: 573px;
    top: 316px;
    text-align: center;
    font-family: "Open Sans", sans-serif;
    color: var(--text-grey);
  }
  .person-name {
    font-size: 39px;
    letter-spacing: 9px;
    line-height: 44px;
  }
  .person-title {
    font-size: 25px;
    line-height: 30px;
    margin-left: -8px;
  }
  .contact-list {
    position: absolute;
    left: 566px;
    top: 424px;
    list-style: none;
    font-family: "Open Sans", sans-serif;
    font-size: 26px;
    color: var(--text-grey);
  }
  .contact-item {
    display: flex;
    align-items: center;
    height: 40px;
  }
  .contact-icon {
    width: 22px;
    height: 22px;
    margin-right: 37px;
    flex: none;
  }
</style>
</head>
<body>
  <main class="business-card">
    <svg class="card-backdrop" viewBox="0 0 605 363" preserveAspectRatio="none" aria-hidden="true">
      <path d="M0 0 H245 C140 90 140 273 245 363 H0 Z" fill="var(--navy)"/>
      <path d="M0 0 C30 150 110 300 245 363 H0 Z" fill="var(--bright-blue)"/>
      <path d="M0 200 C80 200 180 300 245 363 H0 Z" fill="var(--mid-blue)" opacity="0.6"/>
    </svg>

    <div class="side-wordmark">MORVALYTICS</div>

    <div class="brand-name">MORVALYTICS</div>

    <section class="person">
      <p class="person-name">Proprietor's Name</p>
      <p class="person-title">Proprietor's Title</p>
    </section>

    <ul class="contact-list">
      <li class="contact-item">
        <svg class="contact-icon" viewBox="0 0 24 24" aria-hidden="true">
          <circle cx="12" cy="12" r="10" fill="none" stroke="currentColor" stroke-width="1.8"/>
          <path d="M8.5 7.5 C8 10.5 11 15 15.5 16 L16.5 14.5 L14.5 13 L13.5 14 C12 13.2 10.8 12 10 10.5 L11 9.5 L9.7 7.3 Z" fill="currentColor"/>
        </svg>
        <span>+123 456 789</span>
      </li>
      <li class="contact-item">
        <svg class="contact-icon" viewBox="0 0 24 24" aria-hidden="true">
          <rect x="2" y="5" width="20" height="14" fill="currentColor"/>
          <path d="M2 5 L12 13 L22 5" fill="none" stroke="#ffffff" stroke-width="1.6"/>
        </svg>
        <span>yourname@email.com</span>
      </li>
      <li class="contact-item">
        <svg class="contact-icon" viewBox="0 0 24 24" aria-hidden="true">
          <g fill="none" stroke="currentColor" stroke-width="1.6">
            <circle cx="12" cy="12" r="10"/>
            <ellipse cx="12" cy="12" rx="4.5" ry="10"/>
            <path d="M2 12 H22 M4 7 H20 M4 17 H20"/>
          </g>
        </svg>
        <span>www.morvalytics.com</span>
      </li>
    </ul>
  </main>
</body>
</html>
```